Optometrist A5 flyer update 2014

We are an optical / optometrist business needing an existing A5 flyer updated. This flyer has been very successful but needs to be renewed.
We are supplying all the original source files including images.
I have included pdf files with annotations on the alteration we would like made.
We are open to suggestions / alterations to the design of the pamphlet.
We are after a modern design appealing to the various ages of our patient base.

```html
<!DOCTYPE html>
<html lang="en">
<head>
<meta charset="utf-8">
<title>Barrow Lane Optical – Flyer</title>
<link href="https://fonts.googleapis.com/css2?family=Ubuntu:ital,wght@0,300;0,400;0,500;0,700;1,700&display=swap" rel="stylesheet">
<style>
  :root {
    --navy: #1b2a8f;
    --navy-deep: #15207a;
    --ink: #111111;
    --peach: #fde7da;
    --grey: #6e6f71;
    --green: #1c9b2c;
    --white: #ffffff;
    --hero-tone: #dfe3ea;
    --hero-warm: #ecd8cc;
  }
  html, body {
    margin: 0;
    padding: 0;
    width: 847px;
    height: 1200px;
    overflow: hidden;
    background: var(--white);
  }
  .flyer {
    position: relative;
    width: 847px;
    height: 1200px;
    overflow: hidden;
    font-family: "Ubuntu", sans-serif;
    color: var(--ink);
    background: var(--white);
  }
  .hero-photo {
    position: absolute;
    left: 430px;
    top: 0;
    width: 417px;
    height: 365px;
    background: linear-gradient(100deg, rgba(255,255,255,0) 0%, var(--hero-tone) 45%, var(--hero-warm) 100%);
  }
  .brand {
    position: absolute;
    left: 62px;
    top: 112px;
    color: var(--navy);
    font-weight: 400;
    line-height: 1;
    margin: 0;
  }
  .brand-line-1 { display: block; font-size: 58px; letter-spacing: -0.8px; }
  .brand-line-2 { display: block; font-size: 112px; letter-spacing: -2px; margin-top: 0; }

  .exam-heading {
    position: absolute;
    left: 68px;
    top: 370px;
    margin: 0;
    font-size: 34px;
    font-weight: 500;
    line-height: 48px;
    letter-spacing: -1.6px;
  }
  .bullet-list {
    list-style: none;
    margin: 0;
    padding: 0;
    position: absolute;
  }
  .bullet-list li {
    position: relative;
    padding-left: 28px;
  }
  .bullet-list li::before {
    content: "";
    position: absolute;
    left: 0;
    width: 10px;
    height: 10px;
    background: var(--navy);
  }
  .exam-list {
    left: 70px;
    top: 496px;
    font-size: 22px;
    line-height: 31px;
    letter-spacing: -0.7px;
  }
  .exam-list li { margin-bottom: 17px; }
  .exam-list li::before { top: 11px; }

  .glasses-photo {
    position: absolute;
    left: 0;
    top: 787px;
    width: 418px;
    height: 213px;
    background: linear-gradient(90deg, #f4f4f4 0%, #e2e2e2 45%, #d8c6b8 100%);
  }

  .services-title {
    position: absolute;
    left: 418px;
    top: 373px;
    width: 429px;
    height: 114px;
    background: var(--navy);
    color: var(--white);
    font-style: italic;
    font-weight: 700;
    font-size: 34px;
    line-height: 42px;
    text-align: center;
    display: flex;
    align-items: center;
    justify-content: center;
    padding-right: 30px;
    box-sizing: border-box;
    margin: 0;
  }
  .services-panel {
    position: absolute;
    left: 418px;
    top: 487px;
    width: 429px;
    height: 513px;
    background: var(--peach);
    font-weight: 300;
    color: #1e1e1e;
  }
  .services-intro {
    position: absolute;
    left: 32px;
    top: 26px;
    margin: 0;
    font-size: 23px;
  }
  .services-list {
    left: 28px;
    top: 80px;
    font-size: 23px;
    line-height: 31px;
  }
  .services-list li { margin-bottom: 22px; padding-left: 27px; }
  .services-list li::before { top: 9px; width: 11px; height: 11px; }

  .footer-bands {
    position: absolute;
    left: 0;
    top: 1000px;
    width: 847px;
    height: 123px;
  }
  .team-mark {
    position: absolute;
    left: 70px;
    top: 1016px;
    width: 94px;
    height: 94px;
    border-radius: 50%;
    background: var(--white);
  }
  .team {
    position: absolute;
    left: 198px;
    top: 1026px;
    color: var(--white);
    margin: 0;
  }
  .team-label { display: block; font-weight: 300; font-size: 20px; line-height: 26px; }
  .team-names { display: block; font-weight: 700; font-size: 24px; line-height: 30px; letter-spacing: 0.3px; }
  .contact {
    position: absolute;
    left: 531px;
    top: 1020px;
    color: var(--white);
    font-weight: 700;
    font-size: 23px;
    line-height: 31px;
    letter-spacing: 0.4px;
    font-style: normal;
    margin: 0;
  }
  .contact-icons {
    position: absolute;
    left: 676px;
    top: 1086px;
  }
  .website {
    position: absolute;
    left: 60px;
    top: 1138px;
    margin: 0;
    color: var(--navy-deep);
    font-weight: 700;
    font-size: 27px;
    letter-spacing: 0.2px;
  }
</style>
</head>
<body>
<main class="flyer">
  <div class="hero-photo" role="img" aria-label="Close-up photograph of a blue eye"></div>

  <h1 class="brand">
    <span class="brand-line-1">Barrow Lane</span>
    <span class="brand-line-2">optical</span>
  </h1>

  <h2 class="exam-heading">Publicare bulk billed<br>eye examination</h2>
  <ul class="bullet-list exam-list">
    <li>Glaucoma assessment</li>
    <li>Diabetes vision assessment</li>
    <li>Cataract assessment</li>
    <li>Macula degeneration<br>assessment</li>
    <li>Digital retinal photography</li>
  </ul>

  <div class="glasses-photo" role="img" aria-label="Photograph of a hand holding spectacles in front of an eye test chart"></div>

  <h2 class="services-title">Independent<br>Optometrists</h2>
  <section class="services-panel">
    <p class="services-intro">Servicing Kelsford since 1989:</p>
    <ul class="bullet-list services-list">
      <li>Over 500 spectacle frames and<br>sunglasses to choose from</li>
      <li>Latest spectacle lens<br>technology</li>
      <li>Contact lenses from all leading<br>suppliers</li>
      <li>Direct billing to private health<br>funds with ClaimPoint</li>
      <li>On site lens fittings to own<br>frames</li>
    </ul>
  </section>

  <svg class="footer-bands" viewBox="0 0 847 123" aria-hidden="true">
    <polygon points="0,0 420,0 500,123 0,123" fill="var(--grey)"/>
    <polygon points="420,0 847,0 847,123 500,123" fill="var(--green)"/>
  </svg>

  <div class="team-mark" aria-hidden="true"></div>
  <p class="team">
    <span class="team-label">Optometrists:</span>
    <span class="team-names">Leon Carvell &amp;</span>
    <span class="team-names">Nick Doranis</span>
  </p>

  <address class="contact">14b Barrow Lane,<br>Kelsford<br>9381 2064</address>

  <svg class="contact-icons" width="140" height="46" viewBox="0 0 140 46" aria-hidden="true">
    <g stroke="var(--white)" stroke-width="3" fill="var(--navy)">
      <circle cx="24" cy="24" r="20"/>
      <circle cx="69" cy="24" r="20"/>
      <circle cx="114" cy="24" r="20"/>
    </g>
    <path d="M14 24 L24 15 L34 24 M17 22 V33 H31 V22" fill="none" stroke="var(--white)" stroke-width="2.5" stroke-linejoin="round"/>
    <path d="M63 14 c-3 2 -4 6 -1 11 c3 5 7 8 11 8 l3 -3 l-4 -4 l-3 2 c-2 -1 -4 -3 -5 -6 l2 -2 l-3 -5 z" fill="var(--white)"/>
    <rect x="104" y="17" width="20" height="14" fill="none" stroke="var(--white)" stroke-width="2.2"/>
    <path d="M104 17 L114 25 L124 17" fill="none" stroke="var(--white)" stroke-width="2.2"/>
  </svg>

  <p class="website">www.barrowlaneoptical.com.au</p>
</main>
</body>
</html>
```